Oven Cleaning Business owner needs business card design

Hi there,
Would like for a business card to be designed for myself, the owner of a professional oven cleaning business on the Sunshine Coast.
Would like it to look sleek, and modern-ish. Bit creative is encouraged too.
Include following:
Name/title: Corin ter Haghe, Owner
Phone number: 1300 482 916
Email: info@hearthshinecrew.com.au
Website: www.hearthshinecrew.com.au

```html
<!DOCTYPE html>
<html lang="en">
<head>
<meta charset="utf-8">
<title>Hearthshine Crew – Business Card</title>
<link rel="stylesheet" href="https://fonts.googleapis.com/css2?family=Questrial&display=swap">
<style>
  :root {
    --teal: #4cc0c9;
    --teal-deep: #3aa9b3;
    --white: #ffffff;
    --ink: #111315;
    --band: #1e1d1f;
    --silver-light: #e4e6e8;
    --silver-dark: #8c9094;
    --backdrop: #2b2f33;
    --card-font: "Questrial", sans-serif;
  }
  html, body {
    margin: 0;
    width: 1200px;
    height: 900px;
    overflow: hidden;
    background: var(--backdrop);
  }
  .canvas {
    width: 1200px;
    height: 900px;
    display: flex;
    flex-direction: column;
    align-items: center;
    justify-content: center;
    gap: 60px;
  }
  .card {
    width: 640px;
    height: 366px;
    border-radius: 22px;
    overflow: hidden;
    box-shadow: 0 14px 30px rgba(0,0,0,0.45);
  }
  .card svg {
    display: block;
    width: 640px;
    height: 366px;
    font-family: var(--card-font);
  }
  .brand-name { fill: var(--ink); font-size: 38px; letter-spacing: 1px; }
  .brand-name--small { font-size: 26px; }
  .holder-name { fill: var(--white); font-size: 27px; }
  .holder-title { fill: var(--white); font-size: 13px; letter-spacing: 2px; }
  .contact-line { fill: var(--ink); font-size: 17px; }
  .contact-icon { fill: none; stroke: var(--ink); stroke-width: 1.4; }
</style>
</head>
<body>
<main class="canvas">

  <!-- Front: brand side -->
  <section class="card card--front" aria-label="Card front">
    <svg viewBox="0 0 640 366" xmlns="http://www.w3.org/2000/svg">
      <defs>
        <linearGradient id="silverFront" x1="0" y1="0" x2="1" y2="1">
          <stop offset="0" stop-color="var(--silver-light)"/>
          <stop offset="0.5" stop-color="var(--silver-dark)"/>
          <stop offset="1" stop-color="var(--silver-light)"/>
        </linearGradient>
      </defs>
      <rect class="front-base" width="640" height="366" fill="var(--teal)"/>
      <rect class="front-band" y="112" width="640" height="142" fill="var(--white)"/>
      <circle class="front-ring" cx="190" cy="183" r="116" fill="var(--white)" stroke="url(#silverFront)" stroke-width="4"/>
      <circle class="brand-dot" cx="150" cy="183" r="34" fill="var(--teal)"/>
      <text class="brand-name" x="200" y="197">HEARTHSHINE CREW</text>
    </svg>
  </section>

  <!-- Back: contact side -->
  <section class="card card--back" aria-label="Card back">
    <svg viewBox="0 0 640 366" xmlns="http://www.w3.org/2000/svg">
      <defs>
        <linearGradient id="silverBack" x1="0" y1="0" x2="0" y2="1">
          <stop offset="0" stop-color="var(--silver-light)"/>
          <stop offset="0.5" stop-color="var(--silver-dark)"/>
          <stop offset="1" stop-color="var(--silver-light)"/>
        </linearGradient>
        <linearGradient id="bandEdge" x1="0" y1="0" x2="0" y2="1">
          <stop offset="0" stop-color="#3a393c"/>
          <stop offset="1" stop-color="var(--band)"/>
        </linearGradient>
      </defs>
      <rect class="back-base" width="640" height="366" fill="var(--teal)"/>
      <path class="back-panel" d="M60 0 H440 C335 70 292 200 300 366 H170 C100 366 60 320 60 250 Z" fill="var(--white)"/>
      <path class="back-band" d="M372 78 H640 V136 H338 C346 115 357 95 372 78 Z" fill="url(#bandEdge)"/>
      <line class="back-band-edge" x1="338" y1="137" x2="640" y2="137" stroke="var(--silver-dark)" stroke-width="2"/>
      <path class="back-arc" d="M478 0 C370 78 328 205 336 366" fill="none" stroke="url(#silverBack)" stroke-width="4"/>

      <circle class="brand-dot" cx="180" cy="110" r="26" fill="var(--teal)"/>
      <text class="brand-name brand-name--small" x="100" y="170">HEARTHSHINE</text>
      <text class="brand-name brand-name--small" x="100" y="202">CREW</text>

      <text class="holder-name" x="400" y="112">Corin ter Haghe</text>
      <text class="holder-title" x="400" y="130" dy="0" visibility="hidden">OWNER</text>
      <text class="holder-title" x="540" y="127" text-anchor="start" visibility="hidden">OWNER</text>
      <text class="holder-title" x="400" y="158" style="fill: var(--ink)">OWNER</text>

      <g class="contact">
        <g class="contact-icon" transform="translate(372 195)">
          <circle cx="0" cy="0" r="8"/>
          <path d="M-3 -4 L-1 -4 L0 -1 L-1 0 Q0 2 1.5 3 L2.5 2 L4 3 V4.5 Q0 5 -3 0 Z" fill="var(--ink)" stroke="none"/>
        </g>
        <text class="contact-line" x="390" y="201">1300 482 916</text>

        <g class="contact-icon" transform="translate(372 233)">
          <circle cx="0" cy="0" r="8"/>
          <rect x="-4.5" y="-3" width="9" height="6"/>
          <path d="M-4.5 -3 L0 0.5 L4.5 -3"/>
        </g>
        <text class="contact-line" x="390" y="239">info@hearthshinecrew.com.au</text>

        <g class="contact-icon" transform="translate(372 271)">
          <circle cx="0" cy="0" r="8"/>
          <circle cx="0" cy="0" r="4.5"/>
          <path d="M-4.5 0 H4.5 M0 -4.5 V4.5"/>
        </g>
        <text class="contact-line" x="390" y="277">www.hearthshinecrew.com.au</text>
      </g>
    </svg>
  </section>

</main>
</body>
</html>
```